!st birthday celebration

Im looking for a celebration type of flyer for our first birthday. something colorful and eye catching but with a vintage feel to it. we are a vintage shop with a friendly atmosphere and always have music playing. I have attached a draft copy i have been working on so far. Thanks

Industry/Entity Type

Shop

```html
<!DOCTYPE html>
<html lang="en">
<head>
<meta charset="utf-8">
<title>Happy 1st Birthday Perch Vintage</title>
<link rel="stylesheet" href="https://fonts.googleapis.com/css2?family=Alfa+Slab+One&family=Big+Shoulders+Display:wght@300&family=Josefin+Sans:wght@600;700&family=Lobster&display=swap">
<style>
  :root {
    --paper: #f4efe2;
    --ink-brown: #3a2a22;
    --teal: #1e8a78;
    --teal-shade: #cfe5df;
    --sky: #2bb2ea;
    --sky-soft: #a6dcf3;
    --pink: #e8197c;
    --lime: #8cc63f;
    --coral: #e94f3a;
    --ornament: #c9bfae;
    --hand: #8a7a6c;
  }
  * { margin: 0; padding: 0; box-sizing: border-box; }
  html, body { width: 859px; height: 1200px; overflow: hidden; background: var(--paper); }
  .flyer { position: relative; width: 859px; height: 1200px; background: var(--paper); overflow: hidden; }
  .frame { position: absolute; inset: 32px 36px; border: 2px solid var(--ink-brown); }
  .corner { position: absolute; width: 96px; height: 110px; background: var(--ornament); border-radius: 6px; }
  .corner--tl { top: 20px; left: 22px; }
  .corner--tr { top: 20px; right: 22px; }
  .corner--bl { bottom: 20px; left: 22px; }
  .corner--br { bottom: 20px; right: 22px; }
  .centered { position: absolute; left: 0; width: 100%; text-align: center; white-space: nowrap; }
  .headline {
    font-family: "Alfa Slab One", serif; color: var(--teal);
    font-size: 82px; line-height: 1; letter-spacing: 2px;
    text-shadow: 3px 3px 0 var(--teal-shade);
  }
  .headline--happy { top: 60px; }
  .headline--birthday { top: 154px; }
  .dotted { position: absolute; left: 78px; width: 703px; height: 4px; }
  .dotted--upper { top: 274px; }
  .dotted--lower { top: 422px; }
  .shop-name {
    top: 300px; font-family: "Big Shoulders Display", sans-serif; font-weight: 300;
    color: var(--sky); font-size: 100px; line-height: 1; letter-spacing: 2px;
  }
  .hand { position: absolute; top: 328px; width: 108px; height: 42px; background: var(--hand); border-radius: 8px; }
  .hand--left { left: 82px; }
  .hand--right { right: 82px; }
  .invite {
    font-family: "Lobster", cursive; color: var(--pink); font-size: 46px; line-height: 74px;
  }
  .invite--first { top: 455px; }
  .invite--second { top: 517px; }
  .swirl { position: absolute; top: 546px; width: 120px; height: 20px; background: var(--sky-soft); border-radius: 10px; }
  .swirl--left { left: 132px; }
  .swirl--right { right: 136px; }
  .rule { position: absolute; left: 82px; width: 698px; height: 3px; background: var(--ink-brown); }
  .rule--top { top: 616px; }
  .rule--bottom { top: 768px; }
  .rule--thick { top: 952px; height: 8px; border-radius: 4px; }
  .event-details {
    font-family: "Josefin Sans", sans-serif; font-weight: 700; color: var(--lime);
    font-size: 54px; line-height: 62px; top: 634px; letter-spacing: 2px;
  }
  .activities {
    top: 810px; font-family: "Alfa Slab One", serif; color: var(--teal);
    font-size: 20.5px; line-height: 40px; letter-spacing: 0.4px;
  }
  .contact {
    top: 980px; font-family: "Josefin Sans", sans-serif; font-weight: 600; color: var(--coral);
    font-size: 38px; line-height: 50px; letter-spacing: 1.5px;
  }
  .scroll { position: absolute; top: 1072px; width: 86px; height: 32px; background: var(--sky); border-radius: 16px; }
  .scroll--left { left: 128px; }
  .scroll--right { right: 128px; }
</style>
</head>
<body>
<main class="flyer">
  <div class="frame"></div>
  <div class="corner corner--tl" role="img" aria-label="Decorative flourish corner ornament"></div>
  <div class="corner corner--tr" role="img" aria-label="Decorative flourish corner ornament"></div>
  <div class="corner corner--bl" role="img" aria-label="Decorative flourish corner ornament"></div>
  <div class="corner corner--br" role="img" aria-label="Decorative flourish corner ornament"></div>

  <h1 class="centered headline headline--happy">HAPPY</h1>
  <h1 class="centered headline headline--birthday">1ST BIRTHDAY</h1>

  <svg class="dotted dotted--upper" viewBox="0 0 703 4"><line x1="2" y1="2" x2="701" y2="2" stroke="#1e8a78" stroke-width="4" stroke-linecap="round" stroke-dasharray="0 16"/></svg>
  <div class="hand hand--left" role="img" aria-label="Vintage engraved pointing hand facing right"></div>
  <h2 class="centered shop-name">PERCH VINTAGE!</h2>
  <div class="hand hand--right" role="img" aria-label="Vintage engraved pointing hand facing left"></div>
  <svg class="dotted dotted--lower" viewBox="0 0 703 4"><line x1="2" y1="2" x2="701" y2="2" stroke="#1e8a78" stroke-width="4" stroke-linecap="round" stroke-dasharray="0 16"/></svg>

  <p class="centered invite invite--first">You are invited to help celebrate in</p>
  <div class="swirl swirl--left" role="img" aria-label="Blue looped swirl ornament"></div>
  <p class="centered invite invite--second">the festivities!</p>
  <div class="swirl swirl--right" role="img" aria-label="Blue looped swirl ornament"></div>

  <div class="rule rule--top"></div>
  <p class="centered event-details">DATE : 19TH &amp; 20TH JULY<br>FROM 11:00AM ONWARDS</p>
  <div class="rule rule--bottom"></div>

  <p class="centered activities">POP UP MARKET STALLS • BEST DRESSED VINTAGE OUTFIT<br>FACE PAINTING • VINTAGE CARS ON DISPLAY • MUSIC<br>REFRESHMENTS • 50S HAIRSTYLES</p>

  <div class="rule rule--thick"></div>

  <p class="centered contact">82 WATTLEBROOK RD, MERRIVALE<br>PH: 54 812....<br>MOBILE: 0412558093</p>
  <div class="scroll scroll--left" role="img" aria-label="Blue scroll flourish ornament"></div>
  <div class="scroll scroll--right" role="img" aria-label="Blue scroll flourish ornament"></div>
</main>
</body>
</html>
```